Homepage for the lumo-pathe Web Application

At the end of this text, you will find a link to a website that is under construction for a webApp that I intend to launch soon. The contest goal is for you to make redesign the homepage in a nice, fresh, modern Style. Only design, no coding necessary. It needs to have a responsive version for small screens like smart phones. Attached is the text for it, and some images that you may use. You are welcome to find or create additional supporting images. You can use PixaVendor.example or similar service to find new images as long as I can purchase the non-exclusive use rights for the images at similar prices. The contest is just for the home page. However, the winner, if I like the work and we can agree on a fair price, could be contracted on a one-on-one basis to do the rest of the site. You are welcome to suggest minor changes like font sizes and minor variations on the Header banner, but that banner is consistent with the user interface of the application therefore should not change too much. The information should flow somewhat continually without much use of side bars or things like that.
https://www.lumo-pathe.example
Sincerely,
Marek D. Holloway

```html
<!DOCTYPE html>
<html lang="en">
<head>
<meta charset="utf-8">
<title>Lumo Pathe — Homepage</title>
<link rel="stylesheet" href="https://fonts.googleapis.com/css2?family=Montserrat:ital,wght@0,300;0,400;0,500;0,600;0,700;0,800;1,300;1,400&family=Lato:wght@400;700&display=swap">
<style>
:root{
  --blue-deep:#0b5aa8;
  --blue:#1478be;
  --blue-hero:#2f7fcb;
  --sky:#17aae3;
  --teal:#5ed2cf;
  --teal-dark:#2fa7ae;
  --orange:#ff7f57;
  --ink:#1b1b1b;
  --grey:#6d6d6d;
  --card:#f4f4f4;
  --mist:#f3f3f3;
  --white:#ffffff;
}
*{box-sizing:border-box;margin:0;padding:0}
html,body{width:1200px;height:4082px;overflow:hidden}
body{font-family:"Montserrat",sans-serif;color:var(--ink);background:var(--white);position:relative}
section,header,footer{position:absolute;left:0;width:1200px}
.abs{position:absolute}
.center{text-align:center;left:0;width:1200px}

/* Hero */
.hero{top:0;height:674px;background:linear-gradient(135deg,#3a86d0 0%,var(--blue-hero) 55%,#2a76c2 100%);overflow:visible}
.brand{left:73px;top:72px;display:flex;align-items:center;gap:10px;font-size:36px;font-weight:500;color:var(--teal);letter-spacing:-.5px;white-space:nowrap}
.brand-dot{width:18px;height:18px;border-radius:50%;background:var(--teal)}
.login{left:1062px;top:44px;color:var(--white);font-size:12px;display:flex;align-items:center;gap:8px}
.nav{left:526px;top:82px;display:flex;gap:22px;font-size:12px;color:var(--white);white-space:nowrap}
.nav .active{border-bottom:1.5px solid var(--white);padding-bottom:4px}
.btn-free{left:1038px;top:76px;width:103px;height:29px;border-radius:15px;background:var(--orange);color:var(--white);font-size:12px;font-weight:700;display:flex;align-items:center;justify-content:center;white-space:nowrap}
.hero-art{left:55px;top:160px;width:535px;height:540px;border-radius:28px;background:linear-gradient(160deg,#bdf3f4 0%,var(--teal) 45%,var(--teal-dark) 100%);opacity:.95;z-index:2}
.hero-copy{left:600px;top:276px;width:560px;white-space:nowrap}
.hero-copy .lead{font-size:37px;font-style:italic;font-weight:300;color:var(--teal);line-height:46px}
.hero-copy .big{font-size:45px;font-weight:800;color:var(--white);line-height:44px;letter-spacing:-1px}
.hero-copy .tail{font-size:43px;font-weight:400;color:var(--teal);line-height:52px;letter-spacing:-.5px}
.btn{display:flex;align-items:center;justify-content:center;border-radius:30px;color:var(--white);white-space:nowrap}
.btn-trial{left:610px;top:490px;width:176px;height:51px;background:var(--orange);font-size:20px}
.btn-app{left:813px;top:490px;width:208px;height:51px;border:2px solid var(--white);font-size:20px}

/* Welcome */
.welcome{top:674px;height:380px}
.eyebrow{top:88px;font-size:12px;color:var(--orange);font-family:"Lato",sans-serif}
.welcome h1{top:106px;font-size:33px;font-weight:600;font-family:"Lato",sans-serif}
.welcome p{left:97px;top:184px;width:984px;font-family:"Lato",sans-serif;font-size:12.5px;line-height:16px;color:#555}
.btn-small{height:35px;background:var(--orange);font-size:10px;font-weight:700;letter-spacing:.5px}
.welcome .btn-small{left:532px;top:283px;width:112px}

/* Pricing */
.pricing{top:1054px;height:604px;background:var(--orange)}
.pricing h2{top:74px;font-size:30px;font-weight:600;color:var(--white)}
.pricing .sub{top:120px;left:400px;width:400px;text-align:center;font-size:11.5px;color:var(--white);line-height:16px}
.plan{top:206px;width:246px;height:281px;background:var(--card);text-align:center}
.plan .name{margin-top:42px;font-size:12px;font-weight:600}
.plan .price{margin-top:10px;font-size:58px;font-weight:700;color:var(--blue);line-height:64px;letter-spacing:-1px}
.plan .price small{font-size:34px;vertical-align:8px;margin-right:4px}
.plan .desc{margin:12px auto 0;width:170px;font-size:11px;color:#888;line-height:15px}
.plan .btn{margin:24px auto 0;width:117px;height:36px;background:var(--blue);font-size:11px;font-weight:700}

/* Blog */
.blog{top:1658px;height:704px}
.blog h2{top:78px;font-size:28px;font-weight:600}
.rule{height:3px;background:var(--ink);width:63px;left:568px}
.blog .rule{top:122px}
.blog .sub{top:146px;left:380px;width:440px;text-align:center;font-size:11px;color:#555;line-height:16px}
.post{top:220px;width:282px}
.post .photo{height:188px}
.post .meta{margin:22px 0 0 16px;font-size:9.5px;font-weight:600}
.post h3{margin:12px 16px 0;font-size:15px;font-weight:600;color:var(--orange);line-height:19px}
.post p{margin:14px 16px 0;font-size:10px;color:#888;line-height:14px}
.post .btn{margin:16px 0 0 14px;width:114px;height:27px;background:var(--orange);font-size:9px;font-weight:700}

/* App band */
.app{top:2362px;height:412px;background:linear-gradient(100deg,var(--blue-deep) 0%,#0f86c9 60%,var(--sky) 100%)}
.app h2{left:141px;top:98px;font-size:32px;font-weight:600;color:var(--white)}
.app p{left:144px;top:165px;width:720px;font-size:12px;color:var(--white);line-height:16px}
.store{top:253px;height:44px;border:2px solid var(--white);border-radius:24px;color:var(--white);font-size:12px;font-weight:600;display:flex;align-items:center;justify-content:center;gap:8px;white-space:nowrap}
.store i{width:12px;height:12px;border-radius:50%;background:var(--white)}
.store.try{background:var(--orange);border-color:var(--orange);font-size:16px;font-weight:700}
.app-art{left:911px;top:31px;width:175px;height:420px;border-radius:30px;background:linear-gradient(160deg,#bff4f2 0%,var(--teal) 55%,var(--teal-dark) 100%);transform:skewY(-14deg);z-index:2}

/* Reviews */
.reviews{top:2774px;height:542px}
.reviews h2{top:66px;font-size:35px;font-weight:600}
.reviews .sub{top:130px;left:340px;width:520px;text-align:center;font-size:12px;color:#333;line-height:16px}
.avatar{left:555px;top:187px;width:70px;height:70px;border-radius:50%;background:linear-gradient(160deg,#3a4a5e,#121820)}
.reviewer{top:260px;font-size:24px;font-weight:600;color:var(--blue)}
.stars{top:292px;left:0;width:1200px;display:flex;justify-content:center;gap:3px}
.quote{top:334px;left:300px;width:580px;text-align:center;font-size:12px;font-style:italic;color:#444;line-height:16px}
.dots{top:440px;left:0;width:1200px;display:flex;justify-content:center;gap:10px}
.dots i{width:6px;height:6px;border-radius:50%;background:#ccc}
.dots i.on{background:#888}
.arrow{top:238px}

/* Contact */
.contact{top:3316px;height:525px;background:var(--mist)}
.contact h2{top:70px;font-size:28px;font-weight:600}
.contact .rule{top:116px;background:var(--blue);height:2px;width:50px;left:590px}
.contact .sub{top:136px;left:340px;width:520px;text-align:center;font-size:11.5px;color:#666;line-height:16px}
.field{left:258px;width:335px;height:36px;background:var(--white);border:1px solid #e2e2e2;font-size:11px;color:#888;padding:10px 16px}
.field.comment{left:617px;width:336px;height:150px;top:215px}
.contact .btn{left:532px;top:420px;width:145px;height:35px;background:var(--orange);font-size:11px;font-weight:700}

/* Footer */
.footer{top:3841px;height:241px;background:linear-gradient(100deg,var(--blue-deep) 0%,#0f86c9 60%,var(--sky) 100%)}
.social{top:59px;width:64px;height:64px;border:2px solid rgba(255,255,255,.8);border-radius:50%;display:flex;align-items:center;justify-content:center}
.social i{width:12px;height:12px;border-radius:50%;background:var(--orange)}
.copy{top:168px;font-size:12px;color:var(--white)}
</style>
</head>
<body>

<header class="hero">
  <div class="abs brand"><span class="brand-dot"></span>Lumo Pathe</div>
  <div class="abs login">Login
    <svg width="18" height="18" viewBox="0 0 18 18" fill="none" stroke="#fff" stroke-width="1.4"><circle cx="9" cy="6" r="4"/><path d="M2 17c0-4 3-6 7-6s7 2 7 6"/></svg>
  </div>
  <nav class="abs nav">
    <span class="active">Home</span><span>About us</span><span>Pricing</span><span>Blog</span><span>FAQS</span><span>Support</span><span>Reviews</span><span>Contact us</span>
  </nav>
  <div class="abs btn-free">Free - Trail</div>
  <div class="abs hero-art" role="img" aria-label="Isometric illustration of a laptop with filing drawers and a man holding a folder"></div>
  <div class="abs hero-copy">
    <div class="lead">Keeping track of all your</div>
    <div class="big">PAPER DOCUMENTS</div>
    <div class="big">&amp; OTHER BELONGINGS</div>
    <div class="tail">has never been easier!</div>
  </div>
  <div class="abs btn btn-trial">Free Trial</div>
  <div class="abs btn btn-app">Download App</div>
</header>

<section class="welcome">
  <div class="abs center eyebrow">FIND ANY DOCUMENT OR ITEM INSTANTLY!</div>
  <h1 class="abs center">Welcome to Lumo Pathe</h1>
  <p class="abs">Lumo-Pathe is a system that allows you to quickly search for the location of every item that you store or file. It is an essential tool for keeping track of paper documentsor any other kind of physical item. You'll have the ability to quickly find any item you're searching for, even years after you've stored it.More importantly, using Lumo-Pathe helps you save considerable space without losing speedy accessibility to your treasured items.</p>
  <div class="abs btn btn-small">READ MORE</div>
</section>

<section class="pricing">
  <h2 class="abs center">Our Pricing Plans</h2>
  <div class="abs sub">Lorem ipsum dolor sit amet, consectetur adipiscing elit. Quid autem habent admirationis, cum prope accesseris</div>
  <div class="abs plan" style="left:209px">
    <div class="name">Starter Plan</div>
    <div class="price"><small>$</small>500</div>
    <div class="desc">Lorem ipsum dolor sit amet, consectetur adipisc aliter in vita</div>
    <div class="btn">Get Starter</div>
  </div>
  <div class="abs plan" style="left:477px">
    <div class="name">Basic Plan</div>
    <div class="price"><small>$</small>1000</div>
    <div class="desc">Lorem ipsum dolor sit amet, consectetur adipisc aliter in vita</div>
    <div class="btn">Get Starter</div>
  </div>
  <div class="abs plan" style="left:745px">
    <div class="name">Basic Plan</div>
    <div class="price"><small>$</small>1500</div>
    <div class="desc">Lorem ipsum dolor sit amet, consectetur adipisc aliter in vita</div>
    <div class="btn">Get Starter</div>
  </div>
</section>

<section class="blog">
  <h2 class="abs center">Lates Blog</h2>
  <div class="abs rule"></div>
  <div class="abs sub">Lorem ipsum dolor sit amet, cu per porro dolore nostro, partem cu per porro integre corpora per ea, tation ornatus mel ad</div>
  <article class="abs post" style="left:141px">
    <div class="photo" role="img" aria-label="Photo of a hand holding a smartphone beside a coffee cup" style="background:linear-gradient(135deg,#e8e4e0,#b9b2ab)"></div>
    <div class="meta">By Admin | 4 January 2021</div>
    <h3>Lorem ipsum dolor sit amet cu per porro dolore nostro</h3>
    <p>Lorem ipsum dolor sit amet, cu per porro dolore nostro, partem integre corpora per ea, tation ornatus mel ad Brute voluptatibus an</p>
    <div class="btn">READ MORE</div>
  </article>
  <article class="abs post" style="left:447px">
    <div class="photo" role="img" aria-label="Photo of two colleagues working at a computer in an office" style="background:linear-gradient(135deg,#3d4550,#1c232c)"></div>
    <div class="meta">By Admin | 4 January 2021</div>
    <h3>Sum dolor sit amet cu per porro dolore nostro</h3>
    <p>Lorem ipsum dolor sit amet, cu per porro dolore nostro, partem integre corpora per ea, tation ornatus mel ad Brute voluptatibus an</p>
    <div class="btn">READ MORE</div>
  </article>
  <article class="abs post" style="left:753px">
    <div class="photo" role="img" aria-label="Photo of a smiling woman looking at her phone" style="background:linear-gradient(135deg,#6b5a45,#d6a43a)"></div>
    <div class="meta">By Admin | 4 January 2021</div>
    <h3>Porro dolore nostro Lorem ipsum dolor sit ametcu per</h3>
    <p>Lorem ipsum dolor sit amet, cu per porro dolore nostro, partem integre corpora per ea, tation ornatus mel ad Brute voluptatibus an</p>
    <div class="btn">READ MORE</div>
  </article>
</section>

<section class="app">
  <h2 class="abs">Download App</h2>
  <p class="abs">Lorem ipsum dolor sit amet, consectetur adipiscing elit. Quid autem habent admirationis cum prope accesseris An hoc usque c um propequaque, aliter in vita cum prope accesseris Lorem ipsum dolor sit amet, consectetur adipiscing elit. Quid autem habent admirationis cum prope accesseris? An hoc usque cum propequaque, aliter in vita cum prope accesseris</p>
  <div class="abs store" style="left:141px;width:146px"><i></i>FRUIT STORE</div>
  <div class="abs store" style="left:301px;width:160px"><i></i>DROID MARKET</div>
  <div class="abs store" style="left:476px;width:187px"><i></i>PANE STORE</div>
  <div class="abs store try" style="left:675px;width:181px">TRY FREE TRAIL</div>
  <div class="abs app-art" role="img" aria-label="Isometric illustration of a smartphone with floating folders"></div>
</section>

<section class="reviews">
  <h2 class="abs center">Customers Reviews</h2>
  <div class="abs sub">Constructio interrete. Quia nec honesto quic quam honestius nec turpi turpius. Tria genera bonorum; Quid iudicant sensus?</div>
  <div class="abs avatar" role="img" aria-label="Customer portrait"></div>
  <div class="abs center reviewer">Dara Whitfield</div>
  <div class="abs stars">
    <svg width="60" height="11" viewBox="0 0 60 11" fill="#ff7f1f"><g id="s"><path d="M5.5 0l1.6 3.5 3.9.4-2.9 2.6.8 3.8-3.4-2-3.4 2 .8-3.8L0 3.9l3.9-.4z"/></g><use href="#s" x="12"/><use href="#s" x="24"/><use href="#s" x="36"/><use href="#s" x="48"/></svg>
  </div>
  <div class="abs quote">Constructio interrete. Quia nec honesto quic quam honestius nec turpi turpius. Tria genera bonorum; Quid iudicant sensus? Quae qui non vident, nihil umquam magnum ac cognitione dignum amaverunt. Dicet pro me ipsa virtus nec untur. Paulum, cum regem</div>
  <div class="abs dots"><i class="on"></i><i></i><i></i><i></i><i></i><i></i><i></i></div>
  <svg class="abs arrow" style="left:134px" width="32" height="56" viewBox="0 0 32 56" fill="none" stroke="#555" stroke-width="2"><path d="M29 2L3 28l26 26"/></svg>
  <svg class="abs arrow" style="left:1016px" width="32" height="56" viewBox="0 0 32 56" fill="none" stroke="#555" stroke-width="2"><path d="M3 2l26 26L3 54"/></svg>
</section>

<section class="contact">
  <h2 class="abs center">Get in Touch</h2>
  <div class="abs rule"></div>
  <div class="abs sub">Lorem ipsum dolor sit amet, consectetur adipiscing elit. Quid autem habent admirationis, Non igitur de improbo, sed de callido improbo quaerimus, qualis</div>
  <div class="abs field" style="top:215px">Name*</div>
  <div class="abs field" style="top:272px">Email*</div>
  <div class="abs field" style="top:327px">Phone*</div>
  <div class="abs field comment">Comment*</div>
  <div class="abs btn">SEND MESSAGE</div>
</section>

<footer class="footer">
  <div class="abs social" style="left:390px"><i></i></div>
  <div class="abs social" style="left:461px"><i></i></div>
  <div class="abs social" style="left:534px"><i></i></div>
  <div class="abs social" style="left:607px"><i></i></div>
  <div class="abs social" style="left:678px"><i></i></div>
  <div class="abs social" style="left:749px">
    <svg width="18" height="13" viewBox="0 0 18 13" fill="none" stroke="#ff7f57" stroke-width="1.6"><rect x="1" y="1" width="16" height="11" rx="1"/><path d="M1 1l8 6 8-6"/></svg>
  </div>
  <div class="abs center copy">© 2021 Company Name All Right Reserved</div>
</footer>

</body>
</html>
```